Corvell Staffing Partners Business Cards

Business cards with logo design for a new recruiting company called "Corvell Staffing Partners"

incorporate RED & BLUE colors

Final design should reflect strength - clean, elegant design

Company name superimposed upon graphic (Greek Columns)

Please see attached Photos!!!

Industry/Entity Type

Business

Font styles to use
Decorative

Colors
ec2027
0555a3
85cae6

Requirements
Must have
• Must look very similar to attached design!!!

Want Company name superimposed upon graphic (Greek Columns)

Tag line at bottom must be included:
"Connecting Ambitious Employers with Outstanding Talent"

```html
<!DOCTYPE html>
<html lang="en">
<head>
<meta charset="utf-8">
<title>Corvell Staffing Partners – Business Card</title>
<link rel="stylesheet" href="https://fonts.googleapis.com/css2?family=Crimson+Pro:wght@400;500&display=swap">
<style>
  :root {
    --page-bg: #e9e6e2;
    --card-bg: #ffffff;
    --brand-blue: #0555a3;
    --name-blue: #1f5fd6;
    --brand-red: #ec2027;
    --ink: #1c1c1c;
    --divider: #f2b9b6;
    --mark-blue: #85cae6;
  }
  * { box-sizing: border-box; margin: 0; padding: 0; }
  html, body {
    width: 1200px; height: 845px; overflow: hidden;
    background: var(--page-bg);
  }
  .canvas {
    width: 1200px; height: 845px;
    display: flex; align-items: center; justify-content: center;
  }
  .business-card {
    position: relative;
    width: 1100px; height: 628px;
    background: var(--card-bg);
    box-shadow: 0 6px 24px rgba(0,0,0,0.18);
    font-family: "Crimson Pro", Georgia, serif;
  }
  .brand-block {
    position: absolute; left: 90px; top: 120px;
    display: flex; align-items: center; gap: 36px;
  }
  .brand-dot {
    width: 70px; height: 70px; border-radius: 50%;
    background: var(--mark-blue);
    flex-shrink: 0;
  }
  .brand-name {
    color: var(--brand-blue);
    font-weight: 400;
    font-size: 64px;
    line-height: 1.08;
  }
  .divider {
    position: absolute; left: 630px; top: 95px;
    width: 2px; height: 260px;
    background: linear-gradient(to bottom, var(--divider), rgba(242,185,182,0));
  }
  .person-name {
    position: absolute; left: 670px; top: 105px;
    color: var(--name-blue);
    font-size: 44px; font-weight: 400;
    white-space: nowrap;
  }
  .contact-list {
    position: absolute; left: 670px; top: 200px;
    list-style: none;
    color: var(--ink);
    font-size: 26px;
  }
  .contact-list li {
    display: flex; align-items: center; gap: 12px;
    height: 44px;
    white-space: nowrap;
  }
  .contact-icon { width: 24px; height: 24px; flex-shrink: 0; }
  .tagline {
    position: absolute; left: 0; right: 0; bottom: 80px;
    text-align: center;
    color: var(--brand-red);
    font-size: 40px; font-weight: 400;
    white-space: nowrap;
  }
</style>
</head>
<body>
<main class="canvas">
  <section class="business-card">
    <div class="brand-block">
      <span class="brand-dot" aria-hidden="true"></span>
      <h1 class="brand-name">Corvell<br>Staffing<br>Partners</h1>
    </div>

    <div class="divider" aria-hidden="true"></div>

    <h2 class="person-name">Daniel R. Whitmore</h2>

    <ul class="contact-list">
      <li>
        <svg class="contact-icon" viewBox="0 0 24 24" aria-hidden="true">
          <circle cx="12" cy="12" r="11" fill="none" stroke="#1c1c1c" stroke-width="1.6"/>
          <path d="M8.5 6.5c-1 .6-1.4 1.8-.9 3.2 1 2.8 3 4.9 5.8 6 1.3.5 2.5.1 3.1-.9l-2-1.8-1.4.9c-1.3-.6-2.4-1.7-3-3l.9-1.4z" fill="#1c1c1c"/>
        </svg>
        <span>512-555-0142</span>
      </li>
      <li>
        <svg class="contact-icon" viewBox="0 0 24 24" aria-hidden="true">
          <rect x="2" y="6" width="20" height="13" rx="1.5" fill="#1c1c1c"/>
          <path d="M3 7l9 7 9-7" fill="none" stroke="#ffffff" stroke-width="1.6"/>
        </svg>
        <span>DWhitmore@CorvellSP.com</span>
      </li>
      <li>
        <svg class="contact-icon" viewBox="0 0 24 24" aria-hidden="true">
          <circle cx="12" cy="12" r="10" fill="#1c1c1c"/>
          <g fill="none" stroke="#ffffff" stroke-width="1.2">
            <ellipse cx="12" cy="12" rx="4.5" ry="10"/>
            <line x1="2" y1="12" x2="22" y2="12"/>
            <line x1="12" y1="2" x2="12" y2="22"/>
          </g>
        </svg>
        <span>www.CorvellSP.com</span>
      </li>
    </ul>

    <p class="tagline">Connecting Ambitious Employers with Outstanding Talent</p>
  </section>
</main>
</body>
</html>
```